Velmar Ops Business Cards

We need to design some upbeat business cards. We are an Industrial Rope Access Company/Height Safety Company that specialize in Rope Access, Confined Space, Anchor Points, Safety Systems, PPE Inspecions and Rigging.
Company name is Velmar Ops Ltd
Card is for Gareth Lomas the Company Director
His mobile number is 027 418 9072 and email is gareth@velmarops.co.nz. Website address is www.velmarops.co.nz.
We will post some pictures below to ensure you get a good idea of what we do.

```html
<!DOCTYPE html>
<html lang="en">
<head>
<meta charset="utf-8">
<title>Velmar Ops Business Cards</title>
<link rel="stylesheet" href="https://fonts.googleapis.com/css2?family=Saira:ital,wght@0,700;1,600;1,700&family=Roboto:wght@400&display=swap">
<style>
  :root {
    --backdrop: #e6e3de;
    --card-white: #f3f3f3;
    --card-dark: #231f20;
    --ink: #1f1c1d;
    --ink-soft: #555555;
    --on-dark: #ffffff;
  }
  * { margin: 0; padding: 0; box-sizing: border-box; }
  html, body {
    width: 1200px;
    height: 960px;
    overflow: hidden;
    background: var(--backdrop);
  }
  .card {
    position: absolute;
    width: 601px;
    height: 344px;
    overflow: hidden;
    box-shadow: 0 3px 8px rgba(0,0,0,0.25);
  }
  .card--front { left: 314px; top: 113px; background: var(--card-dark); }
  .card--back  { left: 311px; top: 472px; background: var(--card-white); }

  .front-shape { position: absolute; inset: 0; }

  .wordmark {
    position: absolute;
    font-family: "Saira", sans-serif;
    font-weight: 700;
    color: var(--ink);
    white-space: nowrap;
    letter-spacing: 0.5px;
  }
  .card--front .wordmark { left: 48px; top: 42px; font-size: 38px; line-height: 1; }
  .card--back .wordmark {
    left: 0; right: 0; top: 124px;
    text-align: center; font-size: 48px; line-height: 1;
  }

  .person {
    position: absolute;
    right: 56px;
    top: 170px;
    text-align: right;
    color: var(--on-dark);
    font-family: "Saira", sans-serif;
    font-style: italic;
  }
  .person__name { font-size: 21px; font-weight: 700; line-height: 24px; }
  .person__role { font-size: 15px; font-weight: 600; line-height: 18px; letter-spacing: 0.6px; }

  .contact {
    position: absolute;
    right: 57px;
    top: 231px;
    list-style: none;
    font-family: "Roboto", sans-serif;
    font-size: 14px;
    color: var(--on-dark);
    text-align: right;
  }
  .contact__item {
    display: flex;
    justify-content: flex-end;
    align-items: center;
    gap: 7px;
    height: 19px;
  }
  .contact__icon { width: 12px; height: 12px; flex: none; }

  .services {
    position: absolute;
    left: 0; right: 0; top: 262px;
    text-align: center;
    font-family: "Roboto", sans-serif;
    font-size: 14.5px;
    line-height: 19px;
    color: var(--ink-soft);
  }
</style>
</head>
<body>

<section class="card card--front">
  <svg class="front-shape" width="601" height="344" viewBox="0 0 601 344">
    <polygon points="0,0 396,0 237,278 0,161" fill="var(--card-white)"/>
    <polyline points="406,0 240,289 0,171" fill="none" stroke="var(--card-white)" stroke-width="3.5"/>
  </svg>
  <div class="wordmark">Velmar Ops</div>
  <div class="person">
    <div class="person__name">Gareth Lomas</div>
    <div class="person__role">Company Director</div>
  </div>
  <ul class="contact">
    <li class="contact__item">027 418 9072
      <svg class="contact__icon" viewBox="0 0 12 12"><rect x="3" y="0.5" width="6.5" height="11" rx="1" fill="none" stroke="#fff" stroke-width="1.2"/><rect x="5.4" y="9.3" width="1.7" height="1" fill="#fff"/></svg>
    </li>
    <li class="contact__item">gareth@velmarops.co.nz
      <svg class="contact__icon" viewBox="0 0 12 12"><rect x="0.5" y="2.5" width="11" height="7.5" fill="#fff"/><polyline points="0.5,2.5 6,7 11.5,2.5" fill="none" stroke="var(--card-dark)" stroke-width="1"/></svg>
    </li>
    <li class="contact__item">www.velmarops.co.nz
      <svg class="contact__icon" viewBox="0 0 12 12"><circle cx="6" cy="6" r="5.5" fill="#fff"/><path d="M3 3.5 L6 4.5 L5 7 L3.5 6.5 Z M7 6.5 L9.5 7.5 L8 10 Z" fill="var(--card-dark)"/></svg>
    </li>
  </ul>
</section>

<section class="card card--back">
  <div class="wordmark">Velmar Ops</div>
  <p class="services">
    Rope Access &bull; Anchor Points &bull; PPE Certification<br>
    Confined Space &bull; Safety Systems &bull; Rigging
  </p>
</section>

</body>
</html>
```